Brantley Metal Roofing INC.

Hello,
I am working with a local business to design them a new website. The designer I had worked with moved to colorado and has taken a new job. He recommended that I try posting my new jobs on here. I would need a design and assistance setting the site up on my hostmerry server. I work by myself and handle the sales side of things and need a designer that can help me out.
This company is a metal roofing business. The current page I made for them is www.brantleymetalinc.example

They would like the new site to be similar to http://www.dovecreekalloy.example

Please let me know if this is something that you could do for us.
Updates

the company wants the site to look very similar to this http://www.dovecreekalloy.exampleis that something you could do, please get in touch with me.Thanks Added Tuesday, January 10, 2017

Industry/Entity Type

Business

Font styles to use
Sans Serif

Colors
ed252d

Requirements
Must have
• the company wants the site to look very similar to this
• http://www.dovecreekalloy.example
• is that something you could do, please get in touch with me.
• Thanks

```html
<!DOCTYPE html>
<html lang="en">
<head>
<meta charset="utf-8">
<title>Brantley Roofing</title>
<link rel="stylesheet" href="https://fonts.googleapis.com/css2?family=Montserrat:wght@400;500;700&family=Open+Sans:wght@400;600;700&display=swap">
<style>
  :root {
    --brand-red: #ed252d;
    --button-red: #c20d12;
    --white: #ffffff;
    --text-gray: #5a5a5a;
    --band-gray: #efefef;
    --footer-dark: #3b3b3b;
    --footer-base: #353535;
    --footer-text: #e6e6e6;
    --footer-muted: #bdbdbd;
  }
  * { margin: 0; padding: 0; box-sizing: border-box; }
  html, body { width: 1054px; height: 1200px; overflow: hidden; background: var(--white); }
  body { position: relative; font-family: "Open Sans", Arial, sans-serif; }

  .tagline-bar {
    position: absolute; left: 0; top: 0; width: 1054px; height: 49px;
    background: var(--brand-red); color: var(--white);
    font-family: Arial, Helvetica, sans-serif; font-size: 16px; letter-spacing: 1px;
    display: flex; align-items: center; justify-content: center;
  }

  .hero {
    position: absolute; left: 0; top: 49px; width: 1054px; height: 455px;
    background: linear-gradient(180deg, #6b625a 0%, #a8927a 30%, #b9a184 55%, #8a7564 78%, #6c5d55 100%);
  }
  .hero-rule { position: absolute; left: 0; top: 504px; width: 1054px; height: 6px; background: var(--brand-red); }

  .brand {
    position: absolute; left: 169px; top: 86px; height: 24px;
    display: flex; align-items: center; gap: 9px;
    color: var(--white); font-family: "Montserrat", Arial, sans-serif; font-weight: 500; font-size: 19px;
  }
  .brand-square { width: 14px; height: 14px; background: var(--white); }

  .main-nav { position: absolute; top: 92px; left: 718px; display: flex; font-family: "Montserrat", Arial, sans-serif; font-size: 8.6px; font-weight: 500; }
  .main-nav a { color: var(--white); text-decoration: none; height: 14px; line-height: 14px; padding: 0 9px; }
  .main-nav a.active { background: var(--brand-red); }

  .slider-arrow { position: absolute; top: 244px; }
  .slider-arrow.prev { left: 29px; }
  .slider-arrow.next { left: 1009px; }

  .slider-caption {
    position: absolute; left: 169px; top: 333px;
    font-family: "Montserrat", Arial, sans-serif; font-weight: 500; font-size: 25px; color: var(--white);
  }

  .service { position: absolute; top: 567px; width: 219px; }
  .service-photo { width: 219px; height: 146px; }
  .service-title { margin-top: 12px; color: var(--brand-red); font-size: 9.6px; font-weight: 400; line-height: 13px; text-transform: uppercase; white-space: normal; }
  .service-text { position: absolute; top: 193px; width: 225px; color: var(--text-gray); font-size: 7.6px; line-height: 13.5px; text-transform: uppercase; }

  .subscribe { position: absolute; left: 0; top: 817px; width: 1054px; height: 107px; background: var(--band-gray); }
  .subscribe-input {
    position: absolute; left: 233px; top: 39px; width: 489px; height: 30px;
    background: var(--white); border: 1px solid #dcdcdc; border-radius: 3px;
    font-family: Arial, sans-serif; font-size: 8px; color: #555; padding-left: 14px; line-height: 28px;
  }
  .subscribe-button {
    position: absolute; left: 729px; top: 39px; width: 87px; height: 29px;
    background: var(--button-red); color: var(--white); border-radius: 3px;
    font-family: Arial, sans-serif; font-weight: 700; font-size: 11px;
    display: flex; align-items: center; justify-content: center;
  }

  .site-footer { position: absolute; left: 0; top: 959px; width: 1054px; height: 196px; background: var(--footer-dark); color: var(--footer-text); font-size: 9.6px; }
  .footer-col { position: absolute; top: 50px; }
  .footer-col h3 { font-weight: 400; font-size: 10px; color: var(--footer-text); margin-bottom: 8px; }
  .footer-col ul { list-style: none; }
  .footer-col li { line-height: 15.5px; }
  .contact-line { line-height: 12px; }
  .muted { color: var(--footer-muted); }
  .map-link { display: flex; align-items: center; gap: 4px; }

  .footer-base { position: absolute; left: 0; top: 1155px; width: 1054px; height: 45px; background: var(--footer-base); border-top: 2px solid #2b2b2b; }
  .copyright { position: absolute; left: 171px; top: 15px; color: var(--white); font-weight: 600; font-size: 10px; }
</style>
</head>
<body>
  <header class="tagline-bar">MANUFACTURERS OF QUALITY BUILDING COMPONENTS</header>

  <section class="hero" role="img" aria-label="Photo of a tan two-storey house with shingled roof, white trim and gutters"></section>
  <div class="hero-rule"></div>

  <div class="brand"><span class="brand-square"></span>Brantley Roofing</div>
  <nav class="main-nav">
    <a class="active">HOME</a>
    <a>ABOUT</a>
    <a>CONTACT US</a>
  </nav>

  <svg class="slider-arrow prev" width="16" height="26" viewBox="0 0 16 26" aria-hidden="true"><path d="M14 1 L2 13 L14 25" fill="none" stroke="#fff" stroke-width="1.4"/></svg>
  <svg class="slider-arrow next" width="16" height="26" viewBox="0 0 16 26" aria-hidden="true"><path d="M2 1 L14 13 L2 25" fill="none" stroke="#fff" stroke-width="1.4"/></svg>

  <div class="slider-caption">Slider Text comes here..</div>

  <article class="service" style="left:171px">
    <div class="service-photo" role="img" aria-label="White farmhouse with silver metal roof on green lawn" style="background:linear-gradient(180deg,#b8c9de 0%,#c9d1d8 45%,#dfe0de 70%,#6f7f3e 100%)"></div>
    <h2 class="service-title" style="width:240px">Complete post frame building packages</h2>
    <p class="service-text">Call us for a quote, or stop in and we can help you design.</p>
  </article>

  <article class="service" style="left:417px">
    <div class="service-photo" role="img" aria-label="Close view of a brown metal shingle roof ridge" style="background:linear-gradient(180deg,#3f4a33 0%,#7a5f4e 35%,#8e6e5e 70%,#6e5448 100%)"></div>
    <h2 class="service-title" style="margin-left:-2px">Residential metal roofing</h2>
    <p class="service-text" style="left:-2px">Super rib, snap-loc and a variety of metal roofing options.</p>
  </article>

  <article class="service" style="left:663px">
    <div class="service-photo" role="img" aria-label="Stucco house with garage door and shingled roof" style="background:linear-gradient(180deg,#9fb3cc 0%,#8a7468 30%,#d8d0c4 55%,#b8b0a6 80%,#9a9894 100%)"></div>
    <h2 class="service-title" style="width:180px">Commercial and agricultural applications</h2>
    <p class="service-text">28 gauge panels are the thickest and strongest in the industry.</p>
  </article>

  <section class="subscribe">
    <div class="subscribe-input">enter your email address to subscribe us</div>
    <div class="subscribe-button">Join Us</div>
  </section>

  <footer class="site-footer">
    <div class="footer-col" style="left:170px">
      <h3>RECENT PROJECTS</h3>
      <ul>
        <li>Curabitur iaculis</li>
        <li>Parturient montes</li>
        <li>Vulputate magna</li>
        <li>Cum sociis natoque</li>
        <li>Nulla varius commodo</li>
      </ul>
    </div>
    <div class="footer-col" style="left:451px">
      <h3 style="margin-left:1px">DOWNLOADS</h3>
      <ul>
        <li>Curabitur iaculis</li>
        <li>Parturient montes</li>
        <li>Vulputate magna</li>
        <li>Cum sociis natoque</li>
        <li>Nulla varius commodo</li>
      </ul>
    </div>
    <div class="footer-col" style="left:738px; top:52px">
      <h3 style="margin-bottom:15px">GET IN TOUCH</h3>
      <p class="contact-line">T (212) 555 55 00</p>
      <p class="contact-line"><span class="muted">Email:</span> sales@yourwebsite.com</p>
      <p class="contact-line muted" style="margin-top:18px; line-height:15px">Your Company LTD</p>
      <p class="contact-line muted" style="line-height:15px">Street nr 100, 4536534, Chicago, US</p>
      <p class="contact-line map-link" style="line-height:15px">
        <svg width="7" height="9" viewBox="0 0 7 9" aria-hidden="true"><path d="M3.5 0.5a3 3 0 0 0-3 3c0 2 3 5 3 5s3-3 3-5a3 3 0 0 0-3-3z" fill="#fff"/><circle cx="3.5" cy="3.5" r="1.1" fill="#3b3b3b"/></svg>
        Open in Map View
      </p>
    </div>
  </footer>
  <div class="footer-base"><p class="copyright">All Rights Reserved 2017</p></div>
</body>
</html>
```